THE MARKETPLACE FOR WAREHOUSE, the new way of doing logistics

We need an avant-garde, modern, minimalist and elegant web design for our company called VELMIRA. This company represents the future of logistics, where users can find multiple offers of spaces (warehouse) in one place and other users can offer their available spaces to generate an extra cash inflow. A sample of this company is www.quobly.com, a US company that has developed this business. The closest thing to this type of business is NESTORIA, since it develops a similar model for people who offer spaces in their homes and people who need a space for a limited time. My domain site is www.velmira.com, where is the logo of my company. spanish- ------------------------------------------------ ---------------------------------------------- We need a web design avant-garde, modern, minimalist and elegant for our company called VELMIRA. This company represents the future of logistics, where users can find multiple offers of spaces (wineries) in one place and other users can offer their available spaces to generate an extra profit. A sample of this company is www.quobly.com, a US company that has developed this business. The closest thing to this type of business is NESTORIA, since it develops a similar model for people who offer spaces in their homes and people who need a space for a limited time. My domain site is www.velmira.com, where is the logo of my company.

Target Market(s)

Companies, entrepreneurs, Companies, entrepreneurs,

Industry/Entity Type

Logistic

Number of Pages Required

5+ page

Colors
0d5aa6
ffffff
000000

Requirements
Must have
• A sober and minimalist homepage type plindo, NeStr. That is intuitive, must have spaces for advertising banners. You must always highlight the company logo. A sober and minimalist homepage like plindo, NeStr. That is intuitive, must have spaces for advertising banners. Must always highlight the company logo.

```html
<!DOCTYPE html>
<html lang="en">
<head>
<meta charset="utf-8">
<title>VELMIRA — Menu</title>
<link rel="stylesheet" href="https://fonts.googleapis.com/css2?family=Anton&family=Oswald:wght@400;600;700&family=Jost:wght@400;500&display=swap">
<style>
  :root {
    --brand: #0d5aa6;
    --brand-light: #1a8fd0;
    --ink: #000000;
    --paper: #ffffff;
    --backdrop: #f3f3f3;
    --rule: #e6e6e6;
    --muted: #e2e2e2;
  }
  html, body {
    margin: 0;
    width: 1200px;
    height: 1200px;
    overflow: hidden;
    background: var(--backdrop);
  }
  .page {
    position: absolute;
    left: 0;
    top: 254px;
    width: 1200px;
    height: 691px;
    background: var(--paper);
    box-shadow: 0 18px 40px rgba(0,0,0,0.12);
    font-family: "Oswald", sans-serif;
    color: var(--ink);
  }
  .rule { position: absolute; background: var(--rule); }
  .rule--v { width: 1px; }
  .rule--h { height: 1px; }

  .brand {
    position: absolute; left: 4px; top: 24px;
    display: flex; align-items: center; gap: 6px;
    font-family: "Oswald", sans-serif; font-weight: 600;
    font-size: 17px; letter-spacing: 1px; color: var(--brand-light);
  }
  .brand__dot {
    width: 18px; height: 18px; border-radius: 50%;
    background: var(--brand);
  }

  .search { position: absolute; left: 842px; top: 28px; }
  .menu-toggle {
    position: absolute; left: 962px; top: 30px;
    display: flex; align-items: center; gap: 14px;
    font-family: "Jost", sans-serif; font-size: 8px; letter-spacing: 6px;
  }
  .favorites {
    position: absolute; right: 7px; top: 32px;
    font-family: "Oswald", sans-serif; font-weight: 700; font-size: 11px;
  }

  .hero-title {
    position: absolute; left: 19px; top: 156px; margin: 0;
    font-family: "Anton", sans-serif; font-weight: 400;
    font-size: 96px; line-height: 1; letter-spacing: -1px;
  }

  .nav {
    position: absolute; left: 19px; top: 425px; margin: 0; padding: 0;
    list-style: none;
  }
  .nav__item {
    font-family: "Oswald", sans-serif; font-weight: 700;
    font-size: 47px; line-height: 58px; color: var(--muted);
    letter-spacing: 0.5px;
  }
  .nav__item--active { color: var(--ink); }

  .photo {
    position: absolute; left: 392px; top: 75px; width: 808px; height: 496px;
    background: linear-gradient(100deg, #8a9aa5 0%, #3e6f44 30%, #5b6b5f 48%, #c6d3dc 70%, #e8eef2 100%);
  }

  .social {
    position: absolute; top: 636px; margin: 0; padding: 0; list-style: none;
    font-family: "Jost", sans-serif; font-size: 7.5px; letter-spacing: 0.2px;
  }
  .auth {
    position: absolute; right: 30px; top: 629px;
    font-family: "Oswald", sans-serif; font-weight: 700; font-size: 15px;
  }
</style>
</head>
<body>
  <main class="page">
    <span class="rule rule--h" style="left:0;top:75px;width:1200px"></span>
    <span class="rule rule--h" style="left:0;top:377px;width:392px"></span>
    <span class="rule rule--v" style="left:238px;top:0;height:691px"></span>
    <span class="rule rule--v" style="left:392px;top:0;height:691px"></span>
    <span class="rule rule--v" style="left:805px;top:0;height:75px"></span>
    <span class="rule rule--v" style="left:900px;top:0;height:691px"></span>

    <header>
      <div class="brand"><span class="brand__dot"></span>VELMIRA</div>
      <svg class="search" width="18" height="18" viewBox="0 0 18 18" aria-label="Search">
        <circle cx="10" cy="7.5" r="6" fill="none" stroke="#000" stroke-width="1.2"/>
        <line x1="5.8" y1="11.8" x2="2" y2="16" stroke="#000" stroke-width="1.2"/>
      </svg>
      <div class="menu-toggle">
        <svg width="9" height="9" viewBox="0 0 9 9" aria-hidden="true">
          <path d="M1 1 8 8M8 1 1 8" stroke="#000" stroke-width="1"/>
        </svg>
        <span>MENU</span>
      </div>
      <div class="favorites">FAVORITES</div>
    </header>

    <h1 class="hero-title">FEATURED</h1>

    <ul class="nav">
      <li class="nav__item nav__item--active">BROWSE ALL</li>
      <li class="nav__item">ABOUT</li>
      <li class="nav__item">BLOG</li>
      <li class="nav__item">GALLERY</li>
    </ul>

    <div class="photo" role="img" aria-label="Aerial view of a city block with warehouse rooftops, parked buses, a tennis court and trees"></div>

    <ul class="social" style="left:536px">FRIENDLINE</ul>
    <ul class="social" style="left:628px">PICTOGRAM</ul>
    <ul class="social" style="left:723px">VIDSTREAM</ul>

    <div class="auth">LOGIN / REGISTER</div>
  </main>
</body>
</html>
```